Dietitian needs awesome business card

I need a contemporary design that's eye catching but professional.
My card is to given to doctors, specialists and patients alike.
I manage patients with chronic diseases
I have uploaded my logo and current business card, I would also like the other Registered Clinical Nutritionist logo incorporated into the design

Target Market(s)

Doctors, specialists and patients

Industry/Entity Type

Healthcare

Contact Information for Business Card

www.brindlecovenutrition.com.au
Ph: 0427 516 903
Fax: 6482 7315
email: marcus.k.wellfare@quorvamail.com
Space on the back of the card with: Appointment date, Appointment time and appointment location

Font styles to use
Serif

Colors
fbee3e
876aae
ffc214

Requirements
Must have
• My Logo
• Registered Clinical Nutritionist Logo
• My 4 locations - Fernhollow Medical Centre, North Kelby Health, Ashcourt Medical, Pinebrook Doctors Surgery
Nice to have
• I like the colours in my current business card

```html
<!DOCTYPE html>
<html lang="en">
<head>
<meta charset="utf-8">
<title>Brindlecove Nutrition &amp; Dietetics – Business Card</title>
<link rel="stylesheet" href="https://fonts.googleapis.com/css2?family=Source+Sans+3:ital,wght@0,400;0,600;1,600&display=swap">
<style>
  :root {
    --stage: #000000;
    --card: #ffffff;
    --navy: #1f2f8f;
    --royal: #1f5fb8;
    --green: #8cc63f;
    --orange: #f0782a;
    --rule: #2a64b8;
  }
  * { margin: 0; padding: 0; box-sizing: border-box; }
  html, body { width: 1200px; height: 900px; overflow: hidden; background: var(--stage); }
  body { position: relative; font-family: "Source Sans 3", "Myriad Pro", sans-serif; }

  .card { position: absolute; background: var(--card); overflow: hidden; }

  /* Front */
  .card-front { left: 116px; top: 275px; width: 477px; height: 293px; border-radius: 0 52px 0 52px; }
  .brand-mark { position: absolute; left: 150px; top: 30px; width: 78px; height: 78px; border-radius: 50%; background: var(--royal); }
  .brand-name { position: absolute; left: 240px; top: 38px; color: var(--navy); font-weight: 400; line-height: 1; }
  .brand-name .line-1 { display: block; font-size: 40px; }
  .brand-name .line-2 { display: block; font-size: 19px; margin-top: 4px; }

  .name-rule { position: absolute; left: 0; right: 0; top: 160px; height: 1.5px; background: var(--rule); }
  .holder-name { position: absolute; right: 34px; top: 150px; padding: 0 4px; background: var(--card); color: var(--green); font-weight: 600; font-size: 16px; line-height: 20px; }

  .credential-badge { position: absolute; left: 46px; top: 188px; width: 60px; height: 60px; background: var(--orange); }

  .contact-list { position: absolute; right: 34px; top: 178px; list-style: none; text-align: right; }
  .contact-list li { display: flex; justify-content: flex-end; align-items: center; gap: 8px; color: var(--navy); font-size: 13px; line-height: 17px; }
  .contact-list svg { width: 11px; height: 11px; flex: none; }

  .role-line { position: absolute; right: 34px; top: 256px; color: var(--green); font-style: italic; font-weight: 600; font-size: 13.5px; }

  /* Back */
  .card-back { left: 622px; top: 276px; width: 477px; height: 292px; border-radius: 52px 0 52px 0; }
  .back-band { position: absolute; left: 0; top: 0; width: 100%; height: 147px;
    background: linear-gradient(118deg, #1a55b0 0%, #1d6fc4 35%, #1a8ec8 60%, #3aa0b0 78%, #7cbf45 100%); }
  .back-brand { position: absolute; left: 0; right: 0; top: 36px; text-align: center; color: #ffffff; line-height: 1; }
  .back-brand .line-1 { display: block; font-size: 48px; }
  .back-brand .line-2 { display: block; font-size: 22px; margin-top: 2px; }

  .appointment { position: absolute; left: 90px; top: 173px; color: var(--navy); font-size: 13.5px; }
  .appointment .field { white-space: nowrap; }
  .appointment .row { display: flex; gap: 10px; margin-bottom: 19px; }
  .dots { display: inline-block; border-bottom: 1.5px dotted var(--navy); height: 11px; vertical-align: baseline; }

  .notice { position: absolute; left: 0; right: 0; top: 239px; text-align: center; color: var(--royal); font-weight: 600; font-size: 14.5px; }
  .back-strip { position: absolute; left: 0; bottom: 0; width: 100%; height: 25px;
    background: linear-gradient(100deg, #1f5a8a 0%, #3d8f6a 30%, #8cc63f 55%, #3d9ab0 80%, #1f6fb0 100%); }
</style>
</head>
<body>

<section class="card card-front" aria-label="Business card front">
  <div class="brand-mark"></div>
  <div class="brand-name"><span class="line-1">Brindlecove</span><span class="line-2">Nutrition &amp; Dietetics</span></div>

  <div class="name-rule"></div>
  <div class="holder-name">Marcus Kellaway</div>

  <div class="credential-badge" aria-hidden="true"></div>

  <ul class="contact-list">
    <li>0427 516 903
      <svg viewBox="0 0 12 12"><path d="M2.5 1l2 2.2-1 1.3c.7 1.4 1.6 2.3 3 3l1.3-1L10 8.5 9 11C4.8 10.6 1.4 7.2 1 3z" fill="var(--green)"/></svg></li>
    <li>6482 7315
      <svg viewBox="0 0 12 12"><rect x="1" y="4" width="10" height="7" rx="1" fill="var(--green)"/><rect x="3" y="1" width="6" height="4" fill="var(--green)"/><rect x="3" y="6" width="6" height="1.3" fill="#fff"/></svg></li>
    <li>marcus.k.wellfare@quorvamail.com
      <svg viewBox="0 0 12 12"><rect x="1" y="2.5" width="10" height="7" fill="var(--green)"/><path d="M1 2.5l5 4 5-4" stroke="#fff" stroke-width="1" fill="none"/></svg></li>
    <li>www.brindlecovenutrition.com.au
      <svg viewBox="0 0 12 12"><circle cx="6" cy="6" r="5" fill="var(--green)"/><path d="M1 6h10M6 1c-2 2.8-2 7.2 0 10M6 1c2 2.8 2 7.2 0 10" stroke="#fff" stroke-width=".8" fill="none"/></svg></li>
  </ul>

  <p class="role-line">Registered Clinical Nutritionist, Nutritionist and Chef</p>
</section>

<section class="card card-back" aria-label="Business card back">
  <div class="back-band" role="img" aria-label="Abstract blue and green light streaks"></div>
  <div class="back-brand"><span class="line-1">Brindlecove</span><span class="line-2">Nutrition &amp; Dietetics</span></div>

  <div class="appointment">
    <div class="row">
      <span class="field">Date: <span class="dots" style="width:102px"></span></span>
      <span class="field">Time: <span class="dots" style="width:112px"></span></span>
    </div>
    <div class="row">
      <span class="field">Location: <span class="dots" style="width:240px"></span></span>
    </div>
  </div>

  <p class="notice">If unable to keep appointment, kindly give 24hrs notice.</p>
  <div class="back-strip" role="img" aria-label="Abstract green and blue light streaks"></div>
</section>

</body>
</html>
```